Payroll Brochure

Create a brochure with the copy i have provided . A simple easy tp read brochure that shows wat we do we handle payroll taxes insurance 401k etc

```html
<!DOCTYPE html>
<html lang="en">
<head>
<meta charset="utf-8">
<title>Halden Payroll Brochure</title>
<link href="https://fonts.googleapis.com/css2?family=Montserrat:wght@400;500;600;700;800&display=swap" rel="stylesheet">
<style>
:root{
  --stage:#4b4b4b;
  --paper:#ffffff;
  --wash:#eef0f2;
  --wash-deep:#dfe3e7;
  --maroon:#7a1f22;
  --maroon-deep:#5e1518;
  --gold:#d9a632;
  --gold-light:#f0cd68;
  --gold-deep:#b5801f;
  --ink:#3a3a3a;
  --ink-soft:#5b5b5b;
  --photo-a:#5d7392;
  --photo-b:#c9d3df;
  --photo-c:#2f3a4d;
}
*{box-sizing:border-box;margin:0;padding:0}
html,body{width:1200px;height:2517px;overflow:hidden}
body{background:var(--stage);font-family:"Montserrat",Arial,sans-serif;color:var(--ink);position:relative}
.panel{position:absolute;left:0;width:1200px}
.panel--cover{top:0;height:840px}
.panel--outer{top:840px;height:840px}
.panel--inner{top:1680px;height:837px}

.page{position:absolute;background:var(--paper);overflow:hidden;box-shadow:0 14px 30px rgba(0,0,0,.35)}
.spread{position:absolute;left:80px;width:1040px;height:735px}
.spread .page{top:0;width:520px;height:735px}
.spread .page--left{left:0}
.spread .page--right{left:520px}
.spread-fold{position:absolute;left:519px;top:0;width:2px;height:735px;background:linear-gradient(90deg,rgba(0,0,0,.12),rgba(0,0,0,0));z-index:3}

/* cover component, 520 x 735 */
.cover{width:520px;height:735px}
.single{left:340px;top:52px}
.wash{position:absolute;inset:0;background:linear-gradient(125deg,var(--wash) 0%,#fafbfc 45%,var(--wash-deep) 100%)}
.cover-art{position:absolute;left:0;top:0;width:520px;height:735px}
.brand{position:absolute;display:flex;align-items:center;gap:8px;font-weight:800;color:var(--maroon);letter-spacing:1px;white-space:nowrap}
.brand-mark{display:block;background:var(--gold)}
.cover .brand{left:318px;top:150px;font-size:34px}
.cover .brand-mark{width:22px;height:22px}
.cover-photo{left:76px;top:116px;width:248px;height:248px;border-radius:50%;background:linear-gradient(140deg,var(--photo-b),var(--photo-a) 55%,var(--photo-c))}
.cover-headline{position:absolute;left:36px;top:505px;width:320px}
.cover-headline .kicker{font-size:22px;font-weight:700;color:var(--gold);letter-spacing:.5px}
.cover-headline .title{font-size:26px;font-weight:800;color:var(--maroon);letter-spacing:.5px;margin-top:2px}
.cover-headline .lede{font-size:14px;color:var(--ink-soft);line-height:1.45;margin-top:8px}
.cover-url{position:absolute;right:30px;bottom:26px;color:#fff;font-size:14px;letter-spacing:1px;font-weight:500}

/* back cover */
.back .brand{left:175px;top:300px;font-size:40px}
.back .brand-mark{width:26px;height:26px}
.back-rule{position:absolute;left:30px;right:30px;top:600px;height:2px;background:var(--maroon)}
.back-contacts{position:absolute;left:30px;right:30px;top:618px;display:flex;justify-content:space-between;align-items:center;font-size:11px;letter-spacing:.8px;color:var(--ink-soft)}
.back-contacts .phone{font-size:17px;font-weight:700;color:var(--maroon)}

/* inner spread */
.photo{position:absolute}
.photo--meeting{left:70px;top:34px;width:310px;height:240px;background:linear-gradient(135deg,var(--photo-b),var(--photo-a) 55%,var(--photo-c));clip-path:polygon(18% 0,82% 0,100% 50%,82% 100%,18% 100%,0 50%)}
.photo--portrait{left:370px;top:480px;width:140px;height:170px;background:linear-gradient(150deg,var(--photo-b),var(--photo-a) 60%,var(--photo-c));clip-path:polygon(22% 0,100% 0,100% 78%,78% 100%,0 100%,0 22%)}
.inner-left .brand{left:268px;top:290px;font-size:28px}
.inner-left .brand-mark{width:18px;height:18px}
.question{position:absolute;left:432px;top:230px;width:176px;height:160px;border-radius:18px;background:linear-gradient(135deg,var(--gold) 0%,var(--gold-deep) 40%,var(--maroon) 100%);z-index:4;display:flex;align-items:center;justify-content:center;padding:14px;color:#fff;font-weight:700;font-size:16px;line-height:1.25;text-align:center;transform:rotate(-6deg)}
.block{position:absolute}
.block h3{font-size:14px;font-weight:800;color:var(--maroon);letter-spacing:.5px;margin-bottom:5px;padding-bottom:3px;border-bottom:2px solid var(--gold);display:inline-block}
.block p{font-size:9.5px;line-height:1.45;color:var(--ink-soft)}
.inner-left .b-process{left:36px;top:335px;width:215px}
.inner-left .b-people{left:270px;top:410px;width:200px}
.inner-left .b-products{left:36px;top:500px;width:215px}
.inner-left .b-flex{left:270px;top:548px;width:200px}
.page-foot{position:absolute;left:0;right:0;bottom:28px;height:20px}
.page-foot .rule{position:absolute;left:0;right:30px;top:9px;height:2px;background:var(--maroon)}
.page-foot .tab{position:absolute;left:20px;top:0;height:20px;padding:0 14px;background:var(--maroon);color:#fff;font-size:9px;font-weight:600;letter-spacing:.8px;display:flex;align-items:center}
.page-foot .num{position:absolute;right:30px;top:-2px;width:26px;height:22px;background:var(--gold);color:var(--maroon);font-size:11px;font-weight:700;display:flex;align-items:center;justify-content:center}
.inner-right .b-flexible{left:110px;top:50px;width:250px}
.inner-right .b-efficient{left:110px;top:150px;width:250px}
.inner-right .b-grow{left:110px;top:245px;width:340px}
.inner-right .b-accurate{left:110px;top:395px;width:250px}
.inner-right .b-complete{left:110px;top:490px;width:250px}
.payroll-tag{position:absolute;left:380px;top:95px;width:140px;height:150px;background:var(--maroon);border-radius:40px 0 0 40px;color:#fff;font-size:18px;font-weight:700;letter-spacing:1px;display:flex;align-items:center;justify-content:center}
.tax-banner{position:absolute;left:110px;top:345px;width:320px;height:30px;background:var(--maroon);color:#fff;font-size:13px;font-weight:700;letter-spacing:.8px;display:flex;align-items:center;padding-left:18px;clip-path:polygon(0 0,100% 0,94% 100%,0 100%)}
.tax-banner::after{content:"";position:absolute;right:0;top:0;width:6px;height:100%;background:var(--gold)}
</style>
</head>
<body>

<section class="panel panel--cover">
  <div class="page cover single">
    <div class="wash" role="img" aria-label="Faded photo of colleagues in an office"></div>
    <svg class="cover-art" viewBox="0 0 520 735" aria-hidden="true">
      <defs>
        <linearGradient id="goldFill" x1="0" y1="0" x2="1" y2="1">
          <stop offset="0" stop-color="#f0cd68"/><stop offset=".5" stop-color="#d9a632"/><stop offset="1" stop-color="#b5801f"/>
        </linearGradient>
        <linearGradient id="redFill" x1="0" y1="0" x2="1" y2="1">
          <stop offset="0" stop-color="#5e1518"/><stop offset="1" stop-color="#a54a22"/>
        </linearGradient>
        <linearGradient id="bandFill" x1="0" y1="0" x2="1" y2="0">
          <stop offset="0" stop-color="#5e1518"/><stop offset="1" stop-color="#7a1f22"/>
        </linearGradient>
      </defs>
      <polygon points="290,140 410,290 300,440 180,290" fill="url(#redFill)"/>
      <polygon points="190,30 400,270 230,470 20,240" fill="url(#goldFill)"/>
      <circle cx="200" cy="240" r="131" fill="#d9a632"/>
      <polygon points="160,735 235,650 520,650 520,735" fill="url(#bandFill)"/>
    </svg>
    <div class="photo cover-photo" role="img" aria-label="Photo of business people shaking hands at a meeting table"></div>
    <div class="brand"><span class="brand-mark"></span>Halden</div>
    <div class="cover-headline">
      <div class="kicker">LOREM IPSUM</div>
      <div class="title">DOLOR SIT AMET,</div>
      <p class="lede">consectetur adipiscing elit, sed do eiusmod tempor incididunt ut labore</p>
    </div>
    <div class="cover-url">WWW.WEBSITE.COM</div>
  </div>
</section>

<section class="panel panel--outer">
  <div class="spread" style="top:52px">
    <div class="page page--left back">
      <div class="wash" role="img" aria-label="Faded photo of a business meeting"></div>
      <div class="brand"><span class="brand-mark"></span>Halden</div>
      <div class="back-rule"></div>
      <div class="back-contacts">
        <span>WWW.WEBSITE.COM</span>
        <span class="phone">123-456-789</span>
        <span>INFO@WEBSITE.COM</span>
      </div>
    </div>
    <div class="page page--right cover">
      <div class="wash" role="img" aria-label="Faded photo of colleagues in an office"></div>
      <svg class="cover-art" viewBox="0 0 520 735" aria-hidden="true">
        <polygon points="290,140 410,290 300,440 180,290" fill="url(#redFill)"/>
        <polygon points="190,30 400,270 230,470 20,240" fill="url(#goldFill)"/>
        <circle cx="200" cy="240" r="131" fill="#d9a632"/>
        <polygon points="160,735 235,650 520,650 520,735" fill="url(#bandFill)"/>
      </svg>
      <div class="photo cover-photo" role="img" aria-label="Photo of business people shaking hands at a meeting table"></div>
      <div class="brand"><span class="brand-mark"></span>Halden</div>
      <div class="cover-headline">
        <div class="kicker">LOREM IPSUM</div>
        <div class="title">DOLOR SIT AMET,</div>
        <p class="lede">consectetur adipiscing elit, sed do eiusmod tempor incididunt ut labore</p>
      </div>
      <div class="cover-url">WWW.WEBSITE.COM</div>
    </div>
    <div class="spread-fold"></div>
  </div>
</section>

<section class="panel panel--inner">
  <div class="spread" style="top:51px">
    <div class="page page--left inner-left">
      <div class="photo photo--meeting" role="img" aria-label="Photo of two colleagues discussing work at a desk"></div>
      <div class="brand"><span class="brand-mark"></span>Halden</div>
      <div class="block b-process">
        <h3>PROCESS</h3>
        <p>Developed over the years, the Halden process has been designed with speed and accuracy in mind. Halden does what's needed to make sure our clients are presented with speedy responses to their questions and produce accurate and timely payrolls. With Halden's reliable, custom designed software, we can easily tailor to your payroll needs.</p>
      </div>
      <div class="block b-people">
        <h3>PEOPLE</h3>
        <p>Halden has gone to great lengths to hire and train a world-class team of experienced payroll and HR professionals that are genuinely interested in making sure our clients receive the very best in service and support.</p>
      </div>
      <div class="block b-products">
        <h3>PRODUCTS</h3>
        <p>Halden has developed a comprehensive suite of products and services that will fit your needs.</p>
      </div>
      <div class="block b-flex">
        <h3>FLEXIBILITY</h3>
        <p>Halden will design HR solutions that meet your specific needs and requirements.</p>
      </div>
      <div class="page-foot"><span class="rule"></span><span class="tab">THE HALDEN ADVANTAGE</span><span class="num">01</span></div>
    </div>
    <div class="page page--right inner-right">
      <div class="block b-flexible">
        <h3>FLEXIBLE</h3>
        <p>Halden's flexible and powerful payroll module allows you the ability to grow your business by meeting your unique needs. Supporting payrolls for very large to very small companies.</p>
      </div>
      <div class="payroll-tag">PAYROLL</div>
      <div class="block b-efficient">
        <h3>EFFICIENT</h3>
        <p>Get payroll done efficiently and accurately by relying on our flexible design to handle even the most complex payroll needs.</p>
      </div>
      <div class="block b-grow">
        <h3>GROW WITHOUT GROWING PAINS</h3>
        <p>Halden's technology and design is able to allow you to scale your business without adding all the incremental costs typically required.</p>
      </div>
      <div class="tax-banner">TAX REPORTING &amp; PAYMENTS</div>
      <div class="block b-accurate">
        <h3>ACCURATE</h3>
        <p>All payroll taxes (federal, state, local) are calculated accurately. Additionally, we determine proper local tax jurisdictions based on the employee home and work addresses.</p>
      </div>
      <div class="block b-complete">
        <h3>COMPLETE</h3>
        <p>Federal, State, and Local withholding taxes as well as State and Federal Unemployment taxes are provided. Tax payments are integrated into the Accounts Payable and General Ledger modules.</p>
      </div>
      <div class="photo photo--portrait" role="img" aria-label="Photo of a smiling businessman with arms crossed"></div>
      <div class="page-foot"><span class="rule"></span><span class="tab">THE HALDEN ADVANTAGE</span><span class="num">02</span></div>
    </div>
    <div class="question">What makes Halden uniquely qualified to be your service provider?</div>
    <div class="spread-fold"></div>
  </div>
</section>

</body>
</html>
```